New Management Consultant needs a Stationery Design

We are in need of a full image & identity design for a management consultancy named Veroka Solutions.

Veroka Solutions is a management consulting business focusing on the mining and resources sector that specialises in Supply Chain, Integrated Planning, Operational Leadership, Health & Safety, Logistics, Accommodation & Facilities Management and Business Process Improvement.

Excerpt from Linkora Profile:

"A Senior Process Improvement Professional, specialising in logistics, with over 20 years experience with a blue chip resource company (iron ore and diamonds). Expertise in operational leadership, logistics, business process improvement and financial management. Outstanding history of successful achievements, especially in mine scheduling system design (patents certified), cost reduction and business improvement.

Senior management role key strengths include exceptional complex problem solving, contract/contractor management, logistics scheduling and the ability to implement process improvement and optimization at all stages in the business cycle."

The overall feel should be "Efficient, Dynamic, Experienced".

The design should communicate Professional, Efficient & Creative (Think outside the box)

We require:

Business Logo
Business Card
E-Business Card (send by email and Mac Contacts)
A4 Letterhead
A4 Follower page
Invoice Template (see attached)
Presentation Template (see attached - colour scheme to be used in all the design components)

ALSO NEED recommendation for standard Font ( to be compatable with MS Word) for corporate communication.

Must Have:
- LETTERHEAD must have the following details on them

Veroka Solutions
PO Box 418, Kelmore WA 6083
M 0428 561 304
E brendan.veroka@tallwire.com

BUSINESS CARD should have the following details

Brendan Holt
Director
Veroka Solutions
PO Box 418, Kelmore WA 6083
M 0428 561 304

Industry/Entity Type

Management Consulting

```html
<!DOCTYPE html>
<html lang="en">
<head>
<meta charset="UTF-8">
<title>Veroka Solutions – Invoice</title>
<link href="https://fonts.googleapis.com/css2?family=Arimo:wght@400;700&display=swap" rel="stylesheet">
<style>
  :root {
    --paper: #ffffff;
    --ink: #6f6f6f;
    --title: #9c9c9c;
    --rule: #a9a9a9;
    --header: #a6a6a6;
    --brand-blue: #3a7fc4;
    --brand-orange: #e05a1c;
  }
  * { margin: 0; padding: 0; box-sizing: border-box; }
  html, body { width: 923px; height: 1200px; overflow: hidden; }
  body {
    position: relative;
    background: var(--paper);
    font-family: "Arimo", Arial, sans-serif;
    color: var(--ink);
  }
  .invoice-title {
    position: absolute; top: 24px; left: 0; width: 100%;
    text-align: center; font-size: 32px; font-weight: 400;
    color: var(--title); letter-spacing: 0.5px;
  }
  .brand {
    position: absolute; left: 65px; top: 118px;
    display: flex; align-items: center; gap: 14px;
  }
  .brand-mark { width: 44px; height: 44px; background: var(--brand-blue); }
  .brand-name { font-size: 26px; font-weight: 700; color: var(--brand-orange); }
  .invoice-meta {
    position: absolute; left: 95px; top: 217px;
    font-size: 13.5px; line-height: 19px;
  }
  .recipient-label { position: absolute; left: 95px; top: 274px; font-size: 13.5px; }
  .recipient-line {
    position: absolute; left: 117px; width: 142px;
    border-top: 1px solid var(--rule);
  }
  .data-table {
    position: absolute; left: 41px; width: 845px;
    border: 1px solid var(--rule);
  }
  .table-header {
    display: flex; height: 27px; background: var(--header);
    color: #fff; font-size: 12px; text-transform: uppercase;
  }
  .table-header span { display: flex; align-items: center; padding-left: 10px; }
  .col-main { width: 585px; }
  .col-side { flex: 1; }
  .table-row { display: flex; height: 25px; font-size: 13px; }
  .table-row span { display: flex; align-items: center; padding-left: 10px; }
  .table-row .col-main { border-right: 1px solid var(--rule); }
  .job-table { top: 423px; height: 53px; }
  .items-table { top: 500px; height: 559px; }
  .items-table .table-body { display: flex; height: calc(100% - 27px); }
  .items-table .table-body .col-main { border-right: 1px solid var(--rule); }
  .total-cell {
    position: absolute; left: 626px; top: 1058px;
    width: 260px; height: 27px;
    border: 1px solid var(--rule); border-top: none;
  }
  .payment-footer {
    position: absolute; left: 0; top: 1108px; width: 100%;
    text-align: center; font-size: 15.5px; line-height: 27px;
    letter-spacing: -0.3px;
  }
  .brand-band { position: absolute; left: 0; bottom: 0; height: 16px; }
  .band-blue { width: 753px; background: var(--brand-blue); }
  .band-orange { left: 758px; right: 0; background: var(--brand-orange); }
</style>
</head>
<body>
  <h1 class="invoice-title">INVOICE</h1>

  <div class="brand">
    <div class="brand-mark"></div>
    <div class="brand-name">Veroka Solutions</div>
  </div>

  <div class="invoice-meta">
    <p>Date: July 23, 2014</p>
    <p>Invoice #0005</p>
  </div>

  <p class="recipient-label">To</p>
  <div class="recipient-line" style="top:328px"></div>
  <div class="recipient-line" style="top:349px"></div>
  <div class="recipient-line" style="top:370px"></div>

  <div class="data-table job-table">
    <div class="table-header">
      <span class="col-main">Job</span>
      <span class="col-side">Payment Terms</span>
    </div>
    <div class="table-row">
      <span class="col-main">Click here to enter text.</span>
      <span class="col-side"></span>
    </div>
  </div>

  <div class="data-table items-table">
    <div class="table-header">
      <span class="col-main">Description</span>
      <span class="col-side">Total</span>
    </div>
    <div class="table-body">
      <div class="col-main"></div>
      <div class="col-side"></div>
    </div>
  </div>
  <div class="total-cell"></div>

  <div class="payment-footer">
    <p>Electronic Transfer Details BSB&nbsp; Account No.</p>
    <p>Thank you for your business!</p>
  </div>

  <div class="brand-band band-blue"></div>
  <div class="brand-band band-orange"></div>
</body>
</html>
```